Business Landing Page for SEO Company

Need the landing page of the website designed - I will provide the copy, will need to include details of my company and the services offered, about us, testimonials, faq, etc., and all these elements will need to be arranged graphically on the page.

I want something similar to this: https://pebrovault.com/

Not in terms of color or theme or anything, but we offer a similar service and want to display similar information.

Th services we provide are:

Premium Links
Monthly Links Subscription
Link Insertions

Need to advertise them on the front page. Additionally need a place for testimonials, company details, etc.,

We already have logo for the website. Please use the attached file to insert the logo within the overal design.

Target Market(s)

SEO marketers and agencies

Number of Pages Required

1 page

```html
<!DOCTYPE html>
<html lang="en">
<head>
<meta charset="utf-8">
<title>Linkora — Link Building Service</title>
<link rel="stylesheet" href="https://fonts.googleapis.com/css2?family=Open+Sans:wght@400;600;700&display=swap">
<style>
:root{
  --ink:#222;
  --muted:#6d7584;
  --accent:#3f7fd6;
  --accent-dark:#4a3fc4;
  --accent-light:#5ab4e4;
  --lavender:#7a86d6;
  --soft:#f0f2fb;
  --faq-bg:#eef5fc;
  --bar:#efefef;
  --line:#e6e6ee;
  --star:#f5c518;
  --white:#fff;
}
*{box-sizing:border-box;margin:0;padding:0}
html,body{width:1200px;height:3673px;overflow:hidden}
body{font-family:"Open Sans",Arial,sans-serif;color:var(--ink);background:var(--white);position:relative}
.abs{position:absolute}

/* header */
.site-header{position:absolute;left:0;top:0;width:1200px;height:95px;background:var(--bar)}
.brand{position:absolute;left:150px;top:30px;font-size:21px;font-weight:700;color:var(--accent);display:flex;align-items:center;gap:6px}
.brand-dot{width:8px;height:8px;background:var(--accent);border-radius:50%}
.btn-outline{position:absolute;display:flex;align-items:center;justify-content:center;border:1.5px solid var(--lavender);border-radius:30px;color:var(--lavender);font-size:11px;font-weight:700;letter-spacing:1.5px;background:transparent}
.header-cta{left:865px;top:23px;width:184px;height:45px}

/* hero */
.hero{position:absolute;left:0;top:95px;width:1200px;height:575px;overflow:hidden}
.hero-bg{position:absolute;inset:0;background:linear-gradient(115deg,#4a46c0 0%,#4f6cd0 45%,#5aa8d8 100%)}
.hero-title{position:absolute;left:0;top:130px;width:1200px;text-align:center;color:var(--white);font-size:40px;line-height:53px;font-weight:400}
.hero-title strong{font-weight:700}
.hero-cta{position:absolute;left:509px;top:352px;width:182px;height:46px;background:var(--white);border-radius:30px;display:flex;align-items:center;justify-content:center;color:var(--lavender);font-size:11px;font-weight:700;letter-spacing:1.5px}

.section-title{position:absolute;left:0;width:1200px;text-align:center;font-size:16px;font-weight:700;letter-spacing:.3px;color:var(--ink)}

/* about */
.about-copy{position:absolute;left:180px;top:842px;width:840px;font-size:13.6px;line-height:28px;color:var(--ink)}
.about-copy p{margin-bottom:13px}

/* services */
.plan{position:absolute;top:1394px;width:344px;height:548px;background:#fafbfe;box-shadow:0 2px 10px rgba(90,100,180,.07)}
.plan-head{height:203px;background:var(--soft);text-align:center;padding-top:44px}
.plan-head svg{width:52px;height:52px}
.plan-name{margin-top:10px;font-size:17px;font-weight:700;letter-spacing:3px;color:var(--ink)}
.plan-features{list-style:none;text-align:center;margin-top:36px;font-size:13.5px;line-height:28px;color:var(--lavender)}
.plan-price{text-align:center;margin-top:26px;color:var(--lavender)}
.plan-price sup{font-size:17px;vertical-align:24px}
.plan-price .amount{font-size:50px;font-weight:400;line-height:1}
.plan-price .per{font-size:16px}
.plan-btn{position:absolute;left:89px;top:447px;width:166px;height:47px;font-size:11px}
.plan--featured{background:var(--white);box-shadow:0 10px 40px rgba(90,80,210,.22)}
.plan--featured .plan-head{background:linear-gradient(45deg,#4b34c0 0%,#4f6cd2 55%,#5cbde8 100%)}
.plan--featured .plan-name{color:var(--white)}
.plan--featured .plan-btn{border:none;color:var(--white);background:linear-gradient(90deg,#4b34c0,#5ab4e4)}

/* testimonials */
.review{position:absolute;top:2140px;width:271px;height:436px;background:var(--white);border:2px solid #ececf0;box-shadow:0 1px 6px rgba(0,0,0,.05)}
.avatar{position:absolute;left:67px;top:36px;width:133px;height:133px;border-radius:50%;border:3px solid #e4e4e8}
.review-name{position:absolute;left:25px;top:215px;font-size:16px;font-weight:600;color:var(--accent)}
.review-company{position:absolute;left:25px;top:245px;font-size:13.5px}
.review-text{position:absolute;left:25px;top:272px;width:225px;font-size:13.5px;line-height:17.5px}
.stars{position:absolute;left:80px;top:393px;display:flex;gap:5px}
.stars svg{width:17px;height:17px}

/* faq */
.faq-item{position:absolute;width:556px;background:var(--faq-bg);border-left:4px solid var(--accent);padding:16px 20px 0 14px;font-size:13.5px}
.faq-q{display:flex;gap:12px;color:var(--ink)}
.faq-a{margin-left:18px;margin-top:2px;color:var(--muted);line-height:19px;width:510px}

/* contact */
.contact-icon{position:absolute;top:3256px;width:66px;height:66px;border:2px solid var(--accent);border-radius:50%;display:flex;align-items:center;justify-content:center}
.contact-icon svg{width:20px;height:20px}
.contact-text{position:absolute;top:3350px;width:300px;text-align:center;font-size:13.5px;line-height:19px;color:var(--muted)}

/* footer */
.site-footer{position:absolute;left:0;top:3563px;width:1200px;height:110px;background:var(--bar);border-top:1px solid #d4d4d4;text-align:center;padding-top:44px;font-size:13.5px}
</style>
</head>
<body>

<header class="site-header">
  <div class="brand"><span class="brand-dot"></span>Linkora</div>
  <a class="btn-outline header-cta">GET STARTED</a>
</header>

<section class="hero">
  <div class="hero-bg" role="img" aria-label="Abstract blue faceted glass architecture backdrop"></div>
  <h1 class="hero-title">Looking to get <strong>access to the best link building</strong><br><strong>service on the planet?</strong></h1>
  <a class="hero-cta">GET STARTED</a>
</section>

<h2 class="section-title" style="top:776px">ABOUT US</h2>
<div class="about-copy">
  <p>Lorem ipsum dolor sit amet consectetur adipisicing elit.</p>
  <p>Aenean commodo ligula eget dolor. Aenean massa. Lorem ipsum dolor sit amet, consec tetuer adipis elit, aliquam eget nibh etlibura. Aenean commodo ligula eget dolor. Aenean massa. Lorem ipsum dolor sit amet, consec tetuer adipis elit, aliquam eget nibh etlibura. Aenean commodo ligula eget dolor. Aenean massa. Lorem ipsum dolor sit amet, consec tetuer adipis elit, aliquam eget nibh etlibura.</p>
  <p>Aenean commodo ligula eget dolor. Aenean massa. Lorem ipsum dolor sit amet, consec tetuer adipis elit, aliquam eget nibh etlibura. Aenean commodo ligula eget dolor. Aenean massa. Lorem ipsum dolor sit amet, consec tetuer adipis elit, aliquam eget nibh etlibura.</p>
  <p>Lorem ipsum dolor sit amet consectetur adipisicing elit. Deserunt, labore molestias ex odio perspiciatis exercitationem reprehenderit fuga aspernatur culpa nulla nesciunt nobis aut quia dolorem architecto deleniti asperiores. Sed quisquam, incidunt esse sunt culpa eligendi quis sint eveniet. Eum dolore quam recusandae odio voluptas.</p>
</div>

<h2 class="section-title" style="top:1310px">SERVICES</h2>

<div class="plan" style="left:48px">
  <div class="plan-head">
    <svg viewBox="0 0 52 52" fill="none" stroke="#4a7fd8" stroke-width="2" stroke-linejoin="round"><path d="M14 10h24l9 11-21 22L5 21z"/><path d="M5 21h42M19 10l-5 11 12 22 12-22-5-11M14 21l5-11M38 21l-5-11"/></svg>
    <div class="plan-name">PREMIUM LINKS</div>
  </div>
  <ul class="plan-features"><li>Easy Installations</li><li>Unlimited support</li><li>Uniqe Elements</li></ul>
  <div class="plan-price"><sup>$</sup><span class="amount">9.99</span> <span class="per">/Month</span></div>
  <a class="btn-outline plan-btn">PURCHASE</a>
</div>

<div class="plan plan--featured" style="left:428px">
  <div class="plan-head">
    <svg viewBox="0 0 52 52" fill="none" stroke="#dfe4ff" stroke-width="2"><rect x="6" y="10" width="40" height="36" rx="2"/><path d="M6 19h40M16 5v9M36 5v9"/><path d="M13 26h4M21 26h4M29 26h4M37 26h2M13 32h4M21 32h4M29 32h4M37 32h2M13 38h4M21 38h4M29 38h4M37 38h2"/></svg>
    <div class="plan-name">MONTHLY LINKS</div>
  </div>
  <ul class="plan-features"><li>Easy Installations</li><li>Unlimited support</li><li>Free Forever</li></ul>
  <div class="plan-price"><sup>$</sup><span class="amount">9.99</span> <span class="per">/Month</span></div>
  <a class="btn-outline plan-btn">PURCHASE</a>
</div>

<div class="plan" style="left:807px">
  <div class="plan-head">
    <svg viewBox="0 0 52 52" fill="none" stroke="#4a7fd8" stroke-width="2.2"><rect x="5" y="25" width="24" height="12" rx="6" transform="rotate(-45 17 31)"/><rect x="23" y="15" width="24" height="12" rx="6" transform="rotate(-45 35 21)"/></svg>
    <div class="plan-name">LINK INSERTIONS</div>
  </div>
  <ul class="plan-features"><li>Easy Installations</li><li>Unlimited support</li><li>Free Forever</li></ul>
  <div class="plan-price"><sup>$</sup><span class="amount">9.99</span> <span class="per">/Month</span></div>
  <a class="btn-outline plan-btn">PURCHASE</a>
</div>

<h2 class="section-title" style="top:2067px">TESTIMONIALS</h2>

<svg width="0" height="0" style="position:absolute"><defs><symbol id="star" viewBox="0 0 20 20"><path fill="#f5c518" d="M10 1l2.6 6 6.4.5-4.9 4.2 1.5 6.3L10 14.7 4.4 18l1.5-6.3L1 7.5 7.4 7z"/></symbol></defs></svg>

<article class="review" style="left:34px">
  <div class="avatar" role="img" aria-label="Customer portrait" style="background:linear-gradient(160deg,#8a7c78,#b4343a)"></div>
  <div class="review-name">Lorem Ipsum</div><div class="review-company">Company Lorem</div>
  <p class="review-text">Lorem ipsum dolor sit amet consectetur adipisicing elit. Repudiandae nostrum consequatur dolorum in, similique consequuntur. Ex illum beatae dolore voluptate!</p>
  <div class="stars"><svg><use href="#star"/></svg><svg><use href="#star"/></svg><svg><use href="#star"/></svg><svg><use href="#star"/></svg><svg><use href="#star"/></svg></div>
</article>
<article class="review" style="left:321px">
  <div class="avatar" role="img" aria-label="Customer portrait" style="background:linear-gradient(160deg,#1a1a1a,#6b4a36)"></div>
  <div class="review-name">Lorem Ipsum</div><div class="review-company">Company Lorem</div>
  <p class="review-text">Lorem ipsum dolor sit amet consectetur adipisicing elit. Repudiandae nostrum consequatur dolorum in, similique consequuntur. Ex illum beatae dolore voluptate!</p>
  <div class="stars"><svg><use href="#star"/></svg><svg><use href="#star"/></svg><svg><use href="#star"/></svg><svg><use href="#star"/></svg><svg><use href="#star"/></svg></div>
</article>
<article class="review" style="left:607px">
  <div class="avatar" role="img" aria-label="Customer portrait" style="background:linear-gradient(160deg,#1e7fb0,#0f4f78)"></div>
  <div class="review-name">Lorem Ipsum</div><div class="review-company">Company Lorem</div>
  <p class="review-text">Lorem ipsum dolor sit amet consectetur adipisicing elit. Repudiandae nostrum consequatur dolorum in, similique consequuntur. Ex illum beatae dolore voluptate!</p>
  <div class="stars"><svg><use href="#star"/></svg><svg><use href="#star"/></svg><svg><use href="#star"/></svg><svg><use href="#star"/></svg><svg><use href="#star"/></svg></div>
</article>
<article class="review" style="left:894px">
  <div class="avatar" role="img" aria-label="Customer portrait" style="background:linear-gradient(160deg,#d6d8d4,#3b4150)"></div>
  <div class="review-name">Lorem Ipsum</div><div class="review-company">Company Lorem</div>
  <p class="review-text">Lorem ipsum dolor sit amet consectetur adipisicing elit. Repudiandae nostrum consequatur dolorum in, similique consequuntur. Ex illum beatae dolore voluptate!</p>
  <div class="stars"><svg><use href="#star"/></svg><svg><use href="#star"/></svg><svg><use href="#star"/></svg><svg><use href="#star"/></svg><svg><use href="#star"/></svg></div>
</article>

<h2 class="section-title" style="top:2691px">FREQUENTLY ASKED QUESTIONS(FAQ)</h2>

<div class="faq-item" style="left:34px;top:2766px;height:113px;padding-top:18px">
  <div class="faq-q"><span>-</span><span>Question One</span></div>
  <p class="faq-a">Question One. Lorem ipsum dolor sit amet consectetur, adipisicing elit. Quia, veniam reprehenderit odio voluptatem consequuntur voluptates maxime laboriosam ea exercitationem ipsa?</p>
</div>
<div class="faq-item" style="left:34px;top:2889px;height:55px;padding-top:17px"><div class="faq-q"><span>+</span><span>Question Two</span></div></div>
<div class="faq-item" style="left:34px;top:2954px;height:56px;padding-top:17px"><div class="faq-q"><span>+</span><span>Question Three</span></div></div>
<div class="faq-item" style="left:34px;top:3018px;height:57px;padding-top:18px"><div class="faq-q"><span>+</span><span>Question Four</span></div></div>

<div class="faq-item" style="left:607px;top:2766px;height:113px;padding-top:18px">
  <div class="faq-q"><span>-</span><span>Question Five</span></div>
  <p class="faq-a">Question Five. Lorem ipsum dolor sit amet consectetur, adipisicing elit. Quia, veniam reprehenderit odio voluptatem consequuntur voluptates maxime laboriosam ea exercitationem ipsa?</p>
</div>
<div class="faq-item" style="left:607px;top:2889px;height:55px;padding-top:17px"><div class="faq-q"><span>+</span><span>Question Six</span></div></div>
<div class="faq-item" style="left:607px;top:2954px;height:56px;padding-top:17px"><div class="faq-q"><span>+</span><span>Question Seven</span></div></div>
<div class="faq-item" style="left:607px;top:3018px;height:57px;padding-top:18px"><div class="faq-q"><span>+</span><span>Question Eight</span></div></div>

<h2 class="section-title" style="top:3189px">CONTACT US</h2>

<div class="contact-icon" style="left:149px"><svg viewBox="0 0 20 20"><path fill="#3f7fd6" d="M10 1a6.5 6.5 0 0 0-6.5 6.5C3.5 12.5 10 19 10 19s6.5-6.5 6.5-11.5A6.5 6.5 0 0 0 10 1zm0 9a2.5 2.5 0 1 1 0-5 2.5 2.5 0 0 1 0 5z"/></svg></div>
<div class="contact-icon" style="left:565px"><svg viewBox="0 0 20 20"><rect x="2" y="4" width="16" height="12" rx="1.5" fill="#3f7fd6"/><path d="M2.5 5l7.5 6 7.5-6" fill="none" stroke="#fff" stroke-width="1.5"/></svg></div>
<div class="contact-icon" style="left:983px"><svg viewBox="0 0 20 20"><path fill="#3f7fd6" d="M5.2 2.2l2.6 3.2-1.6 2.2c.9 2.2 2.6 3.9 4.8 4.8l2.2-1.6 3.2 2.6-1.4 3c-6.8-.2-11.8-5.2-12-12z"/></svg></div>

<div class="contact-text" style="left:32px">Address here<br>Hre goes another</div>
<div class="contact-text" style="left:450px">firstemail@linkora.com<br>anotheremail@linkora.com</div>
<div class="contact-text" style="left:866px">+100 555 0142<br>+100 555 0198</div>

<footer class="site-footer">Copyright © 2021 Linkora - All Rights Reserved</footer>

</body>
</html>
```